Brantwell Group needs a business card design

We need a new business card design using the logo recently selected in a logo competition on Pixel Forum. Our business is a consultancy specializing in aviation and energy and the winning business card design will promote an image of precision and professionalism with creativity.

Please use the logo with the name on the front of the card and use a complementary font. Make the back white with either the light grey or dark grey logo.

Target Market(s)

Senior finance and legal leaders at aviation and energy companies

Industry/Entity Type

Management Consulting

Contact Information for Business Card

Peter Haldane
President
Brantwell Group

www.brantwellgroup.example

(555) 304-6198
ph@brantwellgroup.example

Requirements
Must have
• Professional font that goes well with the logo font

```html
<!DOCTYPE html>
<html lang="en">
<head>
<meta charset="utf-8">
<title>Brantwell Group – Business Card</title>
<link href="https://fonts.googleapis.com/css2?family=Lato:wght@400;700&display=swap" rel="stylesheet">
<style>
  :root {
    --brand-blue: #1a4170;
    --brand-blue-deep: #163a64;
    --mark-lilac: #d3d5e8;
    --paper: #fdfdfd;
    --ink-grey: #555a60;
    --rule-grey: #b9bcc0;
    --stripe-grey: #8d9094;
    --backdrop: #e9eaec;
  }
  * { box-sizing: border-box; margin: 0; padding: 0; }
  html, body {
    width: 1200px;
    height: 800px;
    overflow: hidden;
  }
  body {
    background: var(--backdrop);
    font-family: "Lato", sans-serif;
    position: relative;
  }
  .card {
    position: absolute;
    width: 520px;
    height: 300px;
    border-radius: 3px;
    box-shadow: 0 10px 24px rgba(0,0,0,0.18);
    overflow: hidden;
  }

  /* Blue side */
  .card--blue {
    left: 80px;
    top: 110px;
    background: var(--brand-blue);
  }
  .card--blue .wordmark {
    position: absolute;
    left: 0; right: 0;
    top: 108px;
    text-align: center;
    font-size: 40px;
    font-weight: 400;
    letter-spacing: 3px;
    color: var(--mark-lilac);
  }
  .card--blue .web-rule {
    position: absolute;
    left: 40px; right: 40px;
    bottom: 44px;
    display: flex;
    align-items: center;
    gap: 10px;
    color: var(--mark-lilac);
    font-size: 13px;
    letter-spacing: 0.3px;
  }
  .web-rule .line {
    flex: 1;
    height: 1px;
    background: var(--mark-lilac);
    opacity: 0.8;
  }

  /* White side */
  .card--white {
    left: 600px;
    top: 390px;
    background: var(--paper);
  }
  .card--white .logo-block {
    position: absolute;
    left: 30px;
    top: 0;
    width: 220px;
    height: 240px;
    display: flex;
    align-items: center;
    justify-content: center;
  }
  .logo-block .wordmark {
    font-size: 27px;
    font-weight: 400;
    letter-spacing: 1.5px;
    color: var(--brand-blue);
    white-space: nowrap;
  }
  .card--white .divider {
    position: absolute;
    left: 262px;
    top: 38px;
    width: 1px;
    height: 160px;
    background: var(--rule-grey);
  }
  .contact {
    position: absolute;
    left: 282px;
    top: 42px;
    color: var(--ink-grey);
  }
  .contact .person {
    font-size: 16px;
    font-weight: 700;
    color: var(--brand-blue);
  }
  .contact .role {
    font-size: 12px;
    margin-top: 2px;
  }
  .contact .lines {
    list-style: none;
    margin-top: 22px;
    font-size: 13px;
  }
  .contact .lines li {
    display: flex;
    align-items: center;
    gap: 7px;
    height: 19px;
  }
  .contact .lines svg {
    width: 12px;
    height: 12px;
    flex: none;
    fill: var(--brand-blue-deep);
  }
  .card--white .stripe {
    position: absolute;
    left: 0; right: 0;
    bottom: 42px;
    height: 4px;
    background: var(--stripe-grey);
  }
  .card--white .band {
    position: absolute;
    left: 0; right: 0;
    bottom: 0;
    height: 42px;
    background: var(--brand-blue);
  }
</style>
</head>
<body>

  <section class="card card--blue">
    <div class="wordmark">Brantwell Group</div>
    <div class="web-rule">
      <span class="line"></span>
      <span class="web">www.brantwellgroup.example</span>
      <span class="line"></span>
    </div>
  </section>

  <section class="card card--white">
    <div class="logo-block">
      <span class="wordmark">Brantwell Group</span>
    </div>
    <div class="divider"></div>
    <div class="contact">
      <div class="person">Peter Haldane</div>
      <div class="role">President</div>
      <ul class="lines">
        <li>
          <svg viewBox="0 0 12 12" aria-hidden="true"><path d="M2.2 0.8l2 2.2-1 1.2c.7 1.5 1.8 2.6 3.3 3.3l1.2-1 2.2 2-1.1 1.9C4.9 10.3 1.7 7.1 0.3 3.2z"/></svg>
          <span>(555) 304-6198</span>
        </li>
        <li>
          <svg viewBox="0 0 12 12" aria-hidden="true"><rect x="0.5" y="2" width="11" height="8" rx="1"/><path d="M1 2.6l5 3.8 5-3.8" fill="none" stroke="#fff" stroke-width="1"/></svg>
          <span>ph@brantwellgroup.example</span>
        </li>
        <li>
          <svg viewBox="0 0 12 12" aria-hidden="true"><circle cx="6" cy="6" r="5.5"/><g fill="none" stroke="#fff" stroke-width="0.8"><ellipse cx="6" cy="6" rx="2.3" ry="5.3"/><path d="M0.7 6h10.6M1.5 3.5h9M1.5 8.5h9"/></g></svg>
          <span>www.brantwellgroup.example</span>
        </li>
      </ul>
    </div>
    <div class="stripe"></div>
    <div class="band"></div>
  </section>

</body>
</html>
```